need a business card designed, I work with independent car dealerships throughout the US, I connect them with Buyers ( private investors, banks, credit unions, finance co's etc... ) that want to purchase their loan portfolio's, also consult on cashflow management, business lines of credit etc... looking for a consultant look, but something that attracts small business owners
Dunmore Consulting

```html
<!DOCTYPE html>
<html lang="en">
<head>
<meta charset="utf-8">
<title>Dunmore Consulting – Business Card</title>
<link href="https://fonts.googleapis.com/css2?family=Marcellus&family=Open+Sans:wght@300;400;600&display=swap" rel="stylesheet">
<style>
  :root {
    --paper: #ffffff;
    --ink: #1b1a1c;
    --night: #000000;
    --red: #d7081c;
    --accent-text: #d9453a;
    --grey: #6d6e71;
    --white: #ffffff;
  }
  * { margin: 0; padding: 0; box-sizing: border-box; }
  html, body {
    width: 1200px; height: 1000px; overflow: hidden;
    background: var(--paper);
  }
  .stage { position: relative; width: 1200px; height: 1000px; }
  .card {
    position: absolute; left: 256px; width: 694px; height: 397px;
    overflow: hidden;
    box-shadow: 0 8px 18px rgba(0,0,0,0.18);
  }
  .card--front { top: 61px; background: var(--paper); }
  .card--back { top: 547px; background: var(--night); }

  .swoosh-area {
    position: absolute; left: 100px; top: 158px; width: 594px; height: 239px;
    background: linear-gradient(100deg, var(--red) 0%, #7a0a14 22%, var(--ink) 45%, var(--ink) 100%);
  }

  .brand {
    position: absolute; display: flex; align-items: center; gap: 14px;
    font-family: "Marcellus", serif; letter-spacing: 1px; white-space: nowrap;
  }
  .brand__square { display: block; background: var(--red); }
  .card--front .brand { left: 174px; top: 46px; }
  .card--front .brand__square { width: 26px; height: 26px; }
  .card--front .brand__name { font-size: 37px; color: var(--ink); line-height: 1; }

  .holder {
    position: absolute; left: 100px; top: 110px;
    font-family: "Open Sans", sans-serif; font-weight: 300;
    font-size: 28px; color: var(--ink); letter-spacing: -0.5px;
  }

  .tagline {
    position: absolute; left: 408px; top: 196px;
    font-family: "Marcellus", serif; font-size: 19px; line-height: 28px;
    color: var(--accent-text);
  }

  .contacts {
    position: absolute; left: 380px; top: 278px; list-style: none;
    font-family: "Open Sans", sans-serif; font-size: 20px; color: var(--white);
  }
  .contacts li { display: flex; align-items: center; height: 33px; }
  .contacts li:first-child { font-weight: 600; }
  .contacts svg { width: 18px; height: 18px; margin-right: 10px; flex: none; }

  .card--back .brand {
    left: 0; right: 0; top: 118px; justify-content: center;
  }
  .card--back .brand__square { width: 30px; height: 30px; }
  .card--back .brand__name { font-size: 32px; color: var(--grey); line-height: 1; }
  .website {
    position: absolute; left: 0; right: 0; top: 186px; text-align: center;
    font-family: "Marcellus", serif; font-size: 40px; color: var(--accent-text);
  }
</style>
</head>
<body>
<main class="stage">
  <section class="card card--front">
    <div class="swoosh-area" role="img" aria-label="Decorative red and charcoal swoosh panel"></div>
    <div class="brand">
      <span class="brand__square"></span>
      <span class="brand__name">DUNMORE CONSULTING</span>
    </div>
    <p class="holder">Daniel R Marsh</p>
    <p class="tagline">Excellent Service<br>and Expedited Funding</p>
    <ul class="contacts">
      <li>
        <svg viewBox="0 0 18 18"><rect x="5" y="1" width="8" height="16" rx="1.5" fill="var(--red)"/><rect x="6.5" y="3.5" width="5" height="5" fill="var(--white)"/></svg>
        303 555 0142
      </li>
      <li>
        <svg viewBox="0 0 18 18"><rect x="1" y="2" width="5" height="15" rx="1" fill="var(--red)"/><rect x="7" y="5" width="10" height="12" rx="1" fill="var(--red)"/><rect x="9" y="7" width="6" height="2" fill="var(--white)"/><rect x="9" y="11" width="6" height="4" fill="var(--white)" opacity="0.7"/></svg>
        303 555 0187
      </li>
      <li>
        <svg viewBox="0 0 18 18"><rect x="1" y="4" width="16" height="11" fill="var(--red)"/><path d="M1.5,4.5 L9,10.5 L16.5,4.5" fill="none" stroke="var(--white)" stroke-width="1.4"/></svg>
        dealdesk7@example.com
      </li>
    </ul>
  </section>

  <section class="card card--back">
    <div class="brand">
      <span class="brand__square"></span>
      <span class="brand__name">DUNMORE CONSULTING</span>
    </div>
    <p class="website">www.dunmoreconsulting.com</p>
  </section>
</main>
</body>
</html>
```